Event for Hair Salon Wigs

We are introducing a new division of our hair salon selling hair wigs. We are introducing our clients to our wig line, which are beautiful well crafted wig. These wigs are not like granny's wigs, but wigs for women who want style and are willing to pay extra for beautiful believeable wigs. The event is casual were clients and there friends will be flowing in and out during a sunday afternoon.
The postcard should reflect a nice sunny spring day, but classy not extremely colorful. If you think a photo would add to a better look to the card....let me know and I will upload some.
Thank you
Updates

I have images that was uploaded, but have not been posted to this project. I'm not sure what's going on, but please look out for them. I have been trying to communicate with customer service, but no  response thus far. The cards I have received this far I think have to much of a colored pattern, I would love it if the logo "K Radiant Wigs" took center stage, rather than the word open house. Open House is important, but I don't won't it to be bolder than "wigs." Please leave room for address labels, and if possible, the description of the event should be in little bigger text. Oh, I am open to an abstract lady rather than the images that are uploaded, but if images are used, you don't have to use them all. Believe it or not...I do like simplicity:)                             

Industry/Entity Type

Hair

```html
<!DOCTYPE html>
<html lang="en">
<head>
<meta charset="utf-8">
<title>K Radiant Wigs – Open House</title>
<link rel="stylesheet" href="https://fonts.googleapis.com/css2?family=Exo+2:wght@300;400;700&family=Poiret+One&display=swap">
<style>
  :root {
    --pink: #e4137e;
    --red: #e3202b;
    --ink: #2a2a2a;
    --white: #ffffff;
    --label-yellow: #f2d21b;
    --panel: rgba(255, 255, 255, 0.82);
    --sky-top: #3f95d6;
    --sky-low: #cfe6f2;
    --meadow-light: #c9e29c;
    --meadow: #7fb444;
    --meadow-deep: #4c8a2b;
    --silhouette: #1c1117;
  }
  * { box-sizing: border-box; margin: 0; padding: 0; }
  html, body { width: 1200px; height: 924px; overflow: hidden; }
  body { font-family: "Exo 2", sans-serif; color: var(--ink); }

  .postcard {
    position: relative;
    width: 1200px;
    height: 924px;
    overflow: hidden;
  }
  .meadow-backdrop {
    position: absolute;
    inset: 0;
    background:
      radial-gradient(ellipse 60% 30% at 30% 85%, rgba(255,255,255,0.35), transparent 70%),
      linear-gradient(180deg,
        var(--sky-top) 0%,
        #8cc4e8 14%,
        var(--sky-low) 26%,
        #e6f1dc 31%,
        var(--meadow-light) 40%,
        var(--meadow) 62%,
        var(--meadow-deep) 100%);
  }
  .lady-silhouette {
    position: absolute;
    left: 520px;
    top: 20px;
    width: 160px;
    height: 190px;
    border-radius: 80px 80px 40px 60px;
    background: var(--silhouette);
  }
  .brand-name {
    position: absolute;
    left: 800px;
    top: 30px;
    width: 380px;
    text-align: center;
    font-family: "Exo 2", sans-serif;
    font-weight: 700;
    font-size: 68px;
    line-height: 74px;
    color: var(--red);
  }
  .event-title {
    position: absolute;
    left: 0;
    width: 1200px;
    top: 236px;
    text-align: center;
    font-family: "Poiret One", cursive;
    font-weight: 400;
    font-size: 58px;
    color: var(--pink);
    letter-spacing: 1px;
  }
  .event-date {
    position: absolute;
    left: 0;
    width: 1200px;
    top: 311px;
    text-align: center;
    font-weight: 400;
    font-size: 19px;
    color: var(--ink);
  }
  .event-date sup { font-size: 10px; }

  .invite-frame {
    position: absolute;
    left: 22px;
    top: 350px;
    width: 1156px;
    height: 396px;
    border: 1px solid rgba(255,255,255,0.9);
  }
  .invite-panel {
    position: absolute;
    left: 35px;
    top: 362px;
    width: 1130px;
    height: 373px;
    background: var(--panel);
    padding: 16px 20px;
    font-weight: 300;
    font-size: 21px;
    line-height: 35px;
  }
  .invite-panel strong { font-weight: 700; }
  .invite-panel em { font-style: italic; }
  .invite-greeting { font-weight: 700; }
  .invite-callout {
    text-align: center;
    color: var(--pink);
    font-weight: 700;
    margin-top: 10px;
  }
  .invite-signoff { margin-top: 22px; line-height: 30px; }

  .perks-band {
    position: absolute;
    left: 0;
    top: 802px;
    width: 785px;
    height: 38px;
    background: var(--pink);
    color: var(--white);
    font-weight: 700;
    font-size: 20px;
    line-height: 38px;
    text-align: right;
    padding-right: 20px;
  }
  .band-end {
    position: absolute;
    left: 1162px;
    top: 802px;
    width: 38px;
    height: 38px;
    background: var(--pink);
  }
  .band-rule {
    position: absolute;
    left: 0;
    top: 855px;
    width: 1200px;
    height: 1px;
    background: var(--pink);
  }

  .contact-list {
    position: absolute;
    left: 828px;
    top: 760px;
    list-style: none;
    font-weight: 300;
    font-size: 20px;
    line-height: 29.5px;
    color: var(--white);
  }
  .contact-list li { display: flex; }
  .contact-label { width: 56px; color: var(--label-yellow); }
</style>
</head>
<body>
<main class="postcard">
  <div class="meadow-backdrop" role="img" aria-label="Sunny spring meadow with white daisies under a blue sky"></div>

  <div class="lady-silhouette" role="img" aria-label="Abstract silhouette of a woman with long flowing hair and a rose"></div>

  <div class="brand-name">K Radiant<br>Wigs</div>

  <h1 class="event-title">OPEN HOUSE</h1>
  <p class="event-date">Sunday April 13<sup>th</sup> 2014&nbsp; | &nbsp;11:00am to 3:00pm</p>

  <div class="invite-frame"></div>
  <section class="invite-panel">
    <p class="invite-greeting">Hello</p>
    <p>I would like to cordially invite you to <strong>Salon K</strong> to introduce you to <strong>K Radiant Wigs</strong>. A showroom of some of the finest human and synthetic hair wigs available. Come look, feel and try-on these beautiful wigs. <strong>K Radiant Wigs</strong> can be purchased and ordered the day of the event for an introductory offer of <em>10% off</em> of the total sales. If you bring a friend or donate a gently warn wig for charity, you will receive <em>15% off</em> of the total purchase. Additionally, bring a friend and a gently warn wig and receive <em>20% off</em> of the total purchase.</p>
    <p class="invite-callout">Come join us...you might find a fabulous new look for spring!</p>
    <p class="invite-signoff">Hope to see you,<br><strong>Karen Holt</strong></p>
  </section>

  <div class="perks-band">Light appetizers and Drinks Raffles</div>
  <div class="band-end"></div>
  <div class="band-rule"></div>

  <ul class="contact-list">
    <li><span class="contact-label">W :</span><span>www.kradiantwigs.com</span></li>
    <li><span class="contact-label">M :</span><span>555 014-2290</span></li>
    <li><span class="contact-label">O :</span><span>Salon K<br>4410 Meadow Ln, Ste. B<br>Fairview, Ca 90000</span></li>
  </ul>
</main>
</body>
</html>
```